Website design for online service business

The company provides the following services:
1 - consultancy services on existing products (like tallydesk and brisk 354)
2 - Coaching services - Coach someone on services like using/developing features with existing products, or teach how to be more productive, or improve their business using automation, etc
3 - Training
- Online training on demand on existing products via vokra (like in Tallydesk and brisk 365)
- Online courses through videos lessons and scripts by offering information products where people will need to register and pay in advance to access the online course. (productivity courses for example)

- The goal is for clients to book time with me for one of those areas without too many clicks.
- Clients will be able to Book time using an integration (it would be good to have the layout integrated with the site.) with this https://planner.brisk-suite.example/owa/calendar/BrightKelpStudio1@brightkelpstudio.bookhub.example/bookings/

- there will be areas for which i whish to build a VIP mailing list. It's referenced on the wireframes

References:
https://www.lanternfieldnotes.example/about/about-dorvan/
https://www.pebblecompass.example/
https://tallydeskguide.example/

Target Market(s)

- Small businesses
- Freelancers

Industry/Entity Type

Business

Number of Pages Required

5+ page

Font styles to use
Sans Serif

Colors

Designer to choose colors to be used in the design.

Requirements
Must have
• Must have the design optimized to the less clicks possible to achieve any action
• The colors of the site should follow the logo (provided in attach)
• It should use other color that belong to the same pallet of colors
• Should contain colors that incentivizes people to click and book something
• Images and backgrounds should be made available
• All images sizes and colors should be provided to be able to develop the site according to the design
Nice to have
• The bookings for the time should be integrated within the design. If not possible a redirection to it can work as well.
Should not have
• Links to social media
• Pop-ups
• Intrusive navigations (like navigation bares on the left or right hand side)
• Should not be a template used by many people

```html
<!DOCTYPE html>
<html lang="en">
<head>
<meta charset="utf-8">
<title>Bright Kelp Studio – Book your spot</title>
<link rel="stylesheet" href="https://fonts.googleapis.com/css2?family=Montserrat:wght@500;600&family=Open+Sans:wght@400;600;700&display=swap">
<style>
  :root {
    --brand-blue: #0074a8;
    --accent-orange: #f39200;
    --ink: #333333;
    --text: #4a4a4a;
    --rule: #e6e6e6;
    --box-border: #cccccc;
    --white: #ffffff;
    --footer-bg: #707070;
    --footer-text: #5c5246;
  }
  * { box-sizing: border-box; margin: 0; padding: 0; }
  html, body { width: 867px; height: 1200px; overflow: hidden; background: var(--white); }
  body { position: relative; font-family: "Open Sans", Arial, sans-serif; color: var(--text); }

  .site-header { position: absolute; left: 0; top: 0; width: 867px; height: 59px; border-bottom: 1px solid var(--rule); }
  .brand { position: absolute; left: 91px; top: 19px; display: flex; align-items: center; gap: 6px; color: var(--brand-blue); font-family: "Montserrat", sans-serif; font-weight: 600; font-size: 13px; }
  .brand-mark { width: 12px; height: 12px; background: var(--brand-blue); }
  .main-nav { position: absolute; top: 20px; right: 78px; display: flex; gap: 15px; font-size: 11.5px; }
  .main-nav a { color: var(--brand-blue); text-decoration: none; }

  .section-title { position: absolute; left: 0; width: 867px; text-align: center; font-family: "Montserrat", sans-serif; font-weight: 600; color: var(--ink); }
  .title-main { top: 92px; font-size: 20px; }
  .title-calm { top: 492px; font-size: 20px; }

  .divider { position: absolute; left: 371px; width: 125px; height: 20px; }
  .divider-top { top: 120px; }
  .divider-calm { top: 520px; }

  .intro { position: absolute; left: 72px; top: 156px; width: 725px; font-size: 9.3px; line-height: 18px; }

  .reasons { position: absolute; left: 258px; top: 228px; width: 352px; height: 197px; border: 2px solid var(--rule); padding-top: 15px; text-align: center; font-size: 9.3px; line-height: 24px; }

  .reassure { position: absolute; left: 0; top: 554px; width: 867px; text-align: center; font-family: "Montserrat", sans-serif; font-weight: 500; font-size: 11.5px; color: var(--ink); letter-spacing: 0.3px; }
  .invite { position: absolute; left: 0; top: 588px; width: 867px; text-align: center; font-size: 9.3px; }

  .booking-band { position: absolute; left: 0; top: 667px; width: 867px; height: 490px; background: var(--brand-blue); }
  .booking-form label { position: absolute; color: var(--white); font-weight: 700; font-size: 9px; }
  .field { position: absolute; background: var(--white); border: none; font-family: inherit; font-size: 9px; color: var(--ink); padding: 0 13px; }
  .calendar-icon { position: absolute; left: 394px; top: 223px; width: 25px; height: 26px; }
  .submit { position: absolute; left: 502px; top: 385px; width: 99px; height: 28px; background: var(--white); border: none; font-family: inherit; font-size: 11px; color: var(--ink); letter-spacing: 0.5px; }

  .site-footer { position: absolute; left: 0; top: 1157px; width: 867px; height: 43px; background: var(--footer-bg); font-size: 9px; }
  .copyright { position: absolute; left: 72px; top: 15px; color: var(--footer-text); }
  .footer-link { position: absolute; right: 72px; top: 15px; color: var(--brand-blue); text-decoration: none; }
</style>
</head>
<body>
  <header class="site-header">
    <div class="brand"><span class="brand-mark"></span>Bright Kelp Studio</div>
    <nav class="main-nav"><a href="#">Service</a><a href="#">Blog</a></nav>
  </header>

  <h1 class="section-title title-main">Yes! There´s still a few spots available to do all the work for you</h1>
  <svg class="divider divider-top" viewBox="0 0 125 20" aria-hidden="true">
    <line x1="0" y1="10" x2="44" y2="10" stroke="#f39200" stroke-width="1.5"/>
    <line x1="81" y1="10" x2="125" y2="10" stroke="#f39200" stroke-width="1.5"/>
    <path d="M53 4 Q58 2 62 5 L62 17 Q58 14 53 16 Z M72 4 Q67 2 63 5 L63 17 Q67 14 72 16 Z" fill="#0074a8"/>
  </svg>

  <p class="intro">Hiring this service will have a different result compared to what you might have experienced so far. You will start to see and hear things about your ideas that you have never experienced before. Your ideias will all of a sudden become a real possibility to move forward. After a while you will have your idea turning into reality and that is something that you have never thought possible, maybe because :</p>

  <div class="reasons">
    <p>you tought there was no market</p>
    <p>or</p>
    <p>that there were so many things to do</p>
    <p>or</p>
    <p>that you don´t have the skills to do it</p>
    <p>or even</p>
    <p>There are so many people doing it already, so why bother?</p>
  </div>

  <h2 class="section-title title-calm">Don´t you worry about anything.</h2>
  <svg class="divider divider-calm" viewBox="0 0 125 20" aria-hidden="true">
    <line x1="0" y1="10" x2="44" y2="10" stroke="#f39200" stroke-width="1.5"/>
    <line x1="81" y1="10" x2="125" y2="10" stroke="#f39200" stroke-width="1.5"/>
    <path d="M53 4 Q58 2 62 5 L62 17 Q58 14 53 16 Z M72 4 Q67 2 63 5 L63 17 Q67 14 72 16 Z" fill="#0074a8"/>
  </svg>
  <p class="reassure">I´m here for you !</p>
  <p class="invite">Fill in the information bellow and I will personally reach out to you so that we can discuss about your idea and what I can do for you.</p>

  <section class="booking-band">
    <form class="booking-form">
      <label style="left:267px;top:66px">Name</label>
      <input class="field" type="text" style="left:267px;top:79px;width:334px;height:31px">
      <label style="left:267px;top:138px">Email</label>
      <input class="field" type="text" style="left:267px;top:150px;width:334px;height:32px">
      <label style="left:267px;top:210px">Date:</label>
      <input class="field" type="text" value="01/03/2000" style="left:267px;top:222px;width:123px;height:31px">
      <svg class="calendar-icon" viewBox="0 0 25 26" aria-hidden="true">
        <rect x="1.5" y="4" width="22" height="20.5" rx="2" fill="none" stroke="#fff" stroke-width="2"/>
        <rect x="1.5" y="4" width="22" height="5" fill="#fff"/>
        <rect x="6" y="1" width="2" height="5" fill="#fff"/><rect x="17" y="1" width="2" height="5" fill="#fff"/>
        <g fill="#fff">
          <rect x="4.5" y="11" width="3" height="3"/><rect x="9" y="11" width="3" height="3"/><rect x="13.5" y="11" width="3" height="3"/><rect x="18" y="11" width="3" height="3"/>
          <rect x="4.5" y="15.5" width="3" height="3"/><rect x="9" y="15.5" width="3" height="3"/><rect x="13.5" y="15.5" width="3" height="3"/><rect x="18" y="15.5" width="3" height="3"/>
          <rect x="4.5" y="20" width="3" height="2.5"/><rect x="9" y="20" width="3" height="2.5"/><rect x="13.5" y="20" width="3" height="2.5"/>
        </g>
      </svg>
      <label style="left:443px;top:210px">Time:</label>
      <input class="field" type="text" style="left:443px;top:222px;width:158px;height:31px">
      <label style="left:267px;top:281px">Any information you would like to share:</label>
      <textarea class="field" style="left:267px;top:294px;width:334px;height:72px;resize:none"></textarea>
      <button class="submit" type="button">SIGN UP</button>
    </form>
  </section>

  <footer class="site-footer">
    <span class="copyright">Copyright Bright Kelp Studio 2018</span>
    <a class="footer-link" href="#">Blog</a>
  </footer>
</body>
</html>
```